QuillBackDesk Website Redesign

I'm looking to redesign our website QuillBackDesk.com. The main goal is to give it a fresh design that is easy on the eyes and pushes the users to creating an account.

Our platform is very simple and we only do one thing, we use ai to generate response to customer and product reviews.

See attached file to see the pricing section style.

On the homepage just under the hero section, I would like to include the wording:
"Write replies to the reviews you get on sites like:" then show the logos like we have on our register page: https://app.quillbackdesk.com/public/index.php

Target Market(s)

Business owners with brick and morter business or any business or product that gets online reviews

Industry/Entity Type

reputation management

Number of Pages Required

2 page

Requirements
Must have
• Home page and pricing page

```html
<!DOCTYPE html>
<html lang="en">
<head>
<meta charset="utf-8">
<title>QuillBackDesk — Personalized Review Replies</title>
<link href="https://fonts.googleapis.com/css2?family=Poppins:wght@400;500;600;700&family=Playfair+Display:wght@400;500&display=swap" rel="stylesheet">
<style>
:root{
  --navy:#1f3d99;
  --blue:#1f47a6;
  --bright:#1652e0;
  --ink:#0f1a3d;
  --dark:#0c1a4a;
  --gold:#ffb000;
  --gold-text:#f2b705;
  --cream:#fff9e8;
  --paper:#ffffff;
  --soft:#f6f8fd;
  --line:#dfe3ee;
  --muted:#4a5168;
}
*{box-sizing:border-box;margin:0;padding:0}
html,body{width:1200px;height:4946px;overflow:hidden}
body{position:relative;font-family:"Poppins",sans-serif;color:var(--ink);background:var(--paper)}
.abs{position:absolute}
.serif{font-family:"Playfair Display",serif;font-weight:400}
.section{position:absolute;left:0;width:1200px}
.btn{position:absolute;display:flex;align-items:center;justify-content:center;font-size:11px;font-weight:600;letter-spacing:.5px;border-radius:3px;text-transform:uppercase}
.btn span{font-weight:400}
.btn-navy{background:var(--navy);color:#fff}
.btn-ghost{background:#fff8dc;border:1.5px solid #f4dd8c;color:var(--ink)}
.brand{position:absolute;display:flex;align-items:center;gap:10px;font-weight:600}
.brand-mark{width:30px;height:30px;border:3px solid var(--navy);border-radius:4px}

/* header */
.site-header{top:0;height:66px;border-bottom:1px solid #eef0f5}
.site-header .brand{left:110px;top:16px;font-size:22px;color:var(--navy)}
.nav{position:absolute;left:470px;top:26px;display:flex;gap:22px;font-size:10.5px;color:var(--muted)}
.sign-in{left:908px;top:19px;width:80px;height:31px;border:1.5px solid #9aa3b8;color:var(--ink);font-size:10px}
.try-free{left:996px;top:19px;width:94px;height:31px;background:var(--bright);color:#fff;font-size:10px}

/* hero */
.hero{top:66px;height:510px}
.hero-kicker{left:110px;top:108px;font-size:36px;color:var(--gold-text)}
.hero-title{left:110px;top:150px;font-size:45px;font-weight:700;line-height:48px;color:var(--ink)}
.hero-title em{font-style:normal;color:var(--bright)}
.hero-sub{left:110px;top:264px;font-size:14px;line-height:22px;color:var(--ink)}
.hero-art{left:690px;top:0;width:410px;height:510px;border-radius:200px 200px 0 0;background:radial-gradient(circle at 50% 38%,#2a66ff 0 38%,#f5f7fb 39%)}

/* logo band */
.logos{top:576px;height:171px;background:var(--blue);color:#fff}
.logos-label{left:0;width:1200px;top:54px;text-align:center;font-size:12px;font-weight:500;letter-spacing:.8px}
.logo-row{position:absolute;left:150px;top:88px;width:900px;display:flex;justify-content:space-between;font-size:25px;font-weight:500;color:#fff}
.pointer{position:absolute}

/* benefits */
.benefits{top:747px;height:677px;background:var(--paper)}
.benefits-title{left:0;width:1200px;top:60px;text-align:center;font-size:16px;font-weight:700}
.benefits-text{left:0;width:1200px;top:90px;text-align:center;font-size:15px;line-height:22px}
.card{position:absolute;top:165px;width:228px;height:368px;background:#fff;border-radius:6px;box-shadow:0 4px 16px rgba(20,40,100,.1);text-align:center;padding:6px}
.card-img{width:216px;height:184px;border-radius:3px}
.card h3{margin-top:22px;font-size:17px;font-weight:600;line-height:22px;color:var(--navy)}
.card .rule{width:55px;height:2px;background:var(--navy);margin:8px auto 12px}
.card p{font-size:10px;line-height:15px;color:var(--ink);padding:0 14px}

/* how */
.how{top:1424px;height:844px}
.kicker{left:0;width:1200px;text-align:center;font-size:33px;color:var(--gold-text)}
.headline{left:0;width:1200px;text-align:center;font-size:43px;font-weight:700;line-height:48px;color:var(--ink)}
.steps-panel{left:158px;top:238px;width:885px;height:523px;background:var(--cream);border-radius:6px}
.step{position:absolute;top:58px;width:220px;text-align:center;font-size:11px;line-height:15px}
.step b{display:block;font-family:"Playfair Display",serif;font-weight:400;font-size:13px}
.step-icon{width:60px;height:52px;margin:0 auto 6px;border-radius:6px;background:linear-gradient(135deg,#dfe6fb,#ffe9a8)}
.steps-rule{left:40px;top:192px;width:805px;height:1px;background:#e4dcc0}
.steps-active{left:337px;top:190px;width:210px;height:4px;background:var(--gold)}
.step-body-kicker{left:52px;top:248px;font-size:14px;color:var(--navy)}
.step-body-title{left:52px;top:270px;font-size:34px;font-weight:700;line-height:38px}
.step-body-text{left:52px;top:358px;font-size:12px;line-height:18px}
.step-art{left:440px;top:222px;width:380px;height:270px;border-radius:8px;background:radial-gradient(circle at 60% 45%,#d6def5,#fff9e8 70%)}

/* pricing */
.pricing{top:2268px;height:1072px;background:linear-gradient(180deg,#0b1a4c 0%,#102a6e 60%,#1a3d98 100%);color:#fff}
.pricing .headline{color:#fff}
.gold-rule{left:555px;top:287px;width:90px;height:4px;background:var(--gold)}
.pricing-note{left:0;width:1200px;top:308px;text-align:center;font-size:14px}
.plan{position:absolute;top:364px;width:447px;height:621px;background:#fff;border-radius:8px;color:var(--ink);overflow:hidden}
.plan-head{height:150px;background:#eef2fb;text-align:center;padding-top:22px}
.plan-head h3{font-family:"Playfair Display",serif;font-weight:500;font-size:21px;color:var(--ink);margin-top:10px}
.plan-head p{font-size:11px;color:var(--muted);margin-top:6px}
.price{position:absolute;left:0;width:100%;text-align:center;font-size:18px;font-weight:600}
.price small{font-size:12px;font-weight:400}
.plan-btn{position:absolute;left:55px;width:336px;height:45px;border-radius:3px;display:flex;align-items:center;justify-content:center;color:#fff;font-size:16px;font-weight:600}
.features{position:absolute;left:55px;width:336px;list-style:none}
.features li{display:flex;align-items:center;gap:12px;height:43px;border-bottom:1px solid #e9ecf3;font-size:13px}
.features li:last-child{border-bottom:none}
.tick{width:20px;height:16px;flex:none}

/* faq */
.faq{top:3340px;height:870px}
.faq-col{position:absolute;width:447px}
.faq-item{position:relative;border-bottom:1.5px solid #f4d27a;padding:10px 30px 18px 0;font-size:11.5px;font-weight:500;color:var(--navy)}
.faq-item .toggle{position:absolute;right:8px;top:6px;font-size:18px;color:var(--bright);font-weight:400}
.faq-item p{margin-top:14px;font-size:10px;line-height:15px;font-weight:400;color:var(--muted)}
.faq-photo{left:70px;top:460px;width:1060px;height:410px;background:linear-gradient(180deg,#f2f2f4 0%,#d9cdbf 55%,#b89a7c 100%)}

/* cta */
.cta{top:4210px;height:370px;background:var(--gold);color:#fff;text-align:center}
.cta h2{position:absolute;left:0;width:1200px;top:62px;font-size:52px;font-weight:700;line-height:60px}
.cta p{position:absolute;left:0;width:1200px;top:216px;font-family:"Playfair Display",serif;font-size:19px}

/* footer */
.site-footer{top:4580px;height:366px;background:var(--dark);color:#fff}
.site-footer .brand{left:210px;top:92px;font-size:26px;color:#fff}
.site-footer .brand-mark{border-color:#fff;width:40px;height:40px}
.social{position:absolute;top:172px;width:34px;height:34px;border:1.5px solid #fff;border-radius:50%}
.foot-col{position:absolute;top:92px;font-size:10px;line-height:30px}
.foot-col h4{font-family:"Playfair Display",serif;font-weight:400;font-size:19px;margin-bottom:4px;line-height:28px}
.member{position:absolute;left:873px;width:117px;height:36px;border-radius:18px;display:flex;align-items:center;justify-content:center;font-size:11px;font-weight:600}
.copyright{left:0;width:1200px;top:330px;text-align:center;font-size:9.5px;color:#b8c0dc}
</style>
</head>
<body>

<header class="section site-header">
  <div class="brand"><span class="brand-mark"></span>QuillBackDesk</div>
  <nav class="nav"><span>Why Reply?</span><span>How It Works</span><span>Pricing</span><span>Blog</span></nav>
  <a class="btn sign-in">Sign <span>&nbsp;In</span></a>
  <a class="btn try-free">Try Free</a>
</header>

<section class="section hero">
  <div class="abs serif hero-kicker">Write Personalized</div>
  <h1 class="abs hero-title">Responses To Reviews<br>In 10 Seconds! <em>(No Joke)</em></h1>
  <p class="abs hero-sub">GET STARTED TODAY WITH ONE FREE REPLY TO YOUR<br>REVIEW. NO CREDIT CARD REQUIRED.</p>
  <a class="btn btn-navy" style="left:110px;top:334px;width:133px;height:46px">Get <span>&nbsp;Started</span></a>
  <a class="btn btn-ghost" style="left:251px;top:334px;width:134px;height:46px">Learn <span>&nbsp;More</span></a>
  <div class="abs hero-art" role="img" aria-label="Illustration of a person typing on a laptop at a desk, in front of a large blue circle"></div>
</section>

<section class="section logos">
  <div class="abs logos-label">WRITE REPLIES TO THE REVIEWS YOU GET ON SITES LIKE</div>
  <div class="logo-row"><span>Searchly</span><span>Yelvo</span><span>Craftly</span><span>TrustMark</span><span>Orbitmart</span><span>TripNest</span><span>StayHaven</span></div>
  <svg class="pointer" style="left:1000px;top:170px" width="126" height="90" viewBox="0 0 126 90"><polygon points="0,0 126,0 90,90" fill="#1f47a6"/></svg>
</section>

<section class="section benefits">
  <h2 class="abs benefits-title">ITS' SIMPLE,</h2>
  <p class="abs benefits-text">Our tool writes replies and responses to the reviews your<br>customers leave. Doesn't matter if it's 1 or 5 stars.</p>
  <div class="card" style="left:112px">
    <div class="card-img" role="img" aria-label="Photo of a notebook with SEO sketches beside a coffee cup" style="background:linear-gradient(135deg,#d9d4c9,#8d8578)"></div>
    <h3>Improved<br>SEO</h3><div class="rule"></div>
    <p>Search engines love seeing you leave a reply to your reviews and will give you a boost in their search results and local SEO.</p>
  </div>
  <div class="card" style="left:360px">
    <div class="card-img" role="img" aria-label="Photo of two colleagues talking at a laptop" style="background:linear-gradient(135deg,#b7a28a,#4d4038)"></div>
    <h3>Build Customer<br>Trust</h3><div class="rule"></div>
    <p>Customers want to know there are humans behind your companies product or service. Show them you value their time.</p>
  </div>
  <div class="card" style="left:608px">
    <div class="card-img" role="img" aria-label="Photo of a hand selecting five gold rating stars" style="background:linear-gradient(135deg,#9fb0c8,#e9c86a)"></div>
    <h3>Increase Customer<br>Loyalty</h3><div class="rule"></div>
    <p>Taking the time to reply to a review shows your customers you care about them and their business. Show them some love!</p>
  </div>
  <div class="card" style="left:856px">
    <div class="card-img" role="img" aria-label="Photo of a smiling client meeting with an advisor" style="background:linear-gradient(135deg,#c9d3df,#7a6a5c)"></div>
    <h3>Convert New<br>Customers</h3><div class="rule"></div>
    <p>FACT: Potential customers read reviews before making a decision. Give a good first impression with personalized replies.</p>
  </div>
  <a class="btn btn-navy" style="left:520px;top:569px;width:160px;height:46px">Get Started</a>
</section>

<section class="section how">
  <div class="abs serif kicker" style="top:62px">How it work</div>
  <h2 class="abs headline" style="top:100px">Just three easy step to get<br>started with QuillBackDesk</h2>
  <div class="abs steps-panel">
    <div class="step" style="left:52px"><div class="step-icon"></div><b>STEP #1</b>Create An Account</div>
    <div class="step" style="left:332px"><div class="step-icon"></div><b>STEP #2</b>Copy &amp; Paste The Review</div>
    <div class="step" style="left:612px"><div class="step-icon"></div><b>STEP #3</b>Personalized Response<br>In Seconds</div>
    <div class="abs steps-rule"></div>
    <div class="abs steps-active"></div>
    <div class="abs serif step-body-kicker">STEP #2</div>
    <h3 class="abs step-body-title">We make it<br>way too simple!</h3>
    <p class="abs step-body-text">Just Copy The Customer Review And Paste<br>It Into Your Account Dashboard</p>
    <a class="btn btn-ghost" style="left:52px;top:412px;width:133px;height:45px">Learn <span>&nbsp;More</span></a>
    <div class="abs step-art" role="img" aria-label="Illustration of people assembling a large five-star rating panel"></div>
  </div>
</section>

<section class="section pricing">
  <div class="abs serif kicker" style="top:68px">Plans &amp; Pricing</div>
  <h2 class="abs headline" style="top:112px">Never worry about having to come<br>up with a unique response to each<br>review ever again!</h2>
  <div class="abs gold-rule"></div>
  <p class="abs pricing-note">If your business, product or service receives reviews, this tool will save you hundreds of hours.</p>

  <div class="plan" style="left:143px">
    <div class="plan-head">
      <svg width="44" height="40" viewBox="0 0 24 22"><polygon points="12,1 15,8 23,8.5 17,13.5 19,21 12,17 5,21 7,13.5 1,8.5 9,8" fill="#ffc928"/></svg>
      <h3>Monthly Subscriptions</h3>
      <p>Perfect For Getting Started For One Business/product</p>
    </div>
    <div class="price" style="top:176px">Starts At $9.99 <small>/ Month</small></div>
    <div class="abs" style="left:55px;top:210px;font-size:14px;font-weight:700">50K</div>
    <div class="abs" style="left:336px;top:210px;width:55px;text-align:right;font-size:14px;font-weight:700">700K+</div>
    <div class="abs" style="left:55px;top:240px;width:336px;height:6px;border-radius:3px;background:#e3e6ee"></div>
    <div class="abs" style="left:55px;top:240px;width:80px;height:6px;border-radius:3px;background:var(--navy)"></div>
    <div class="abs" style="left:128px;top:234px;width:18px;height:18px;border-radius:50%;background:#fff;border:3px solid var(--navy)"></div>
    <div class="abs" style="left:0;width:447px;top:272px;text-align:center;font-size:11px;color:var(--muted)">5000 word credits</div>
    <div class="plan-btn" style="top:299px;background:var(--gold)">Start For Free</div>
    <ul class="features" style="top:366px">
      <li><svg class="tick" viewBox="0 0 20 16"><polyline points="2,8 8,14 18,2" fill="none" stroke="#1652e0" stroke-width="3"/></svg>Personalized responses</li>
      <li><svg class="tick" viewBox="0 0 20 16"><polyline points="2,8 8,14 18,2" fill="none" stroke="#1652e0" stroke-width="3"/></svg>30+ Languages</li>
      <li><svg class="tick" viewBox="0 0 20 16"><polyline points="2,8 8,14 18,2" fill="none" stroke="#1652e0" stroke-width="3"/></svg>Auto-Save</li>
      <li><svg class="tick" viewBox="0 0 20 16"><polyline points="2,8 8,14 18,2" fill="none" stroke="#1652e0" stroke-width="3"/></svg>Revision History</li>
      <li><svg class="tick" viewBox="0 0 20 16"><polyline points="2,8 8,14 18,2" fill="none" stroke="#1652e0" stroke-width="3"/></svg>Assign members usage limits</li>
    </ul>
  </div>

  <div class="plan" style="left:611px">
    <div class="plan-head">
      <svg width="92" height="40" viewBox="0 0 50 22"><polygon points="12,1 15,8 23,8.5 17,13.5 19,21 12,17 5,21 7,13.5 1,8.5 9,8" fill="#ffc928"/><polygon points="38,1 41,8 49,8.5 43,13.5 45,21 38,17 31,21 33,13.5 27,8.5 35,8" fill="#ffc928"/></svg>
      <h3>Agency Subscriptions</h3>
      <p>Perfect For Multiple Clients/products Per Month</p>
    </div>
    <div class="price" style="top:196px">Starting at $75.00 <small>/ month</small></div>
    <div class="plan-btn" style="top:258px;background:var(--navy)">Start For Free</div>
    <ul class="features" style="top:324px">
      <li><svg class="tick" viewBox="0 0 20 16"><polyline points="2,8 8,14 18,2" fill="none" stroke="#1652e0" stroke-width="3"/></svg>Everything in the Startup plan</li>
      <li><svg class="tick" viewBox="0 0 20 16"><polyline points="2,8 8,14 18,2" fill="none" stroke="#1652e0" stroke-width="3"/></svg>Dedicated Account Manager</li>
      <li><svg class="tick" viewBox="0 0 20 16"><polyline points="2,8 8,14 18,2" fill="none" stroke="#1652e0" stroke-width="3"/></svg>Onboarding &amp; Training</li>
      <li><svg class="tick" viewBox="0 0 20 16"><polyline points="2,8 8,14 18,2" fill="none" stroke="#1652e0" stroke-width="3"/></svg>Unlimited Integrations</li>
    </ul>
  </div>
  <svg class="pointer" style="left:70px;top:1071px" width="130" height="90" viewBox="0 0 130 90"><polygon points="0,0 130,0 40,90" fill="#1a3d98"/></svg>
</section>

<section class="section faq">
  <div class="abs serif kicker" style="top:70px">Faq's</div>
  <h2 class="abs headline" style="top:108px">Frequetnly asked questions</h2>
  <div class="faq-col" style="left:110px;top:240px">
    <div class="faq-item">Why Is It Important To Respond To Searchly Reviews?<span class="toggle">+</span></div>
    <div class="faq-item" style="margin-top:30px">How can I trust someone who doesn't work at my business<br>to reply to reviews on my behalf?<span class="toggle">−</span>
      <p>Building trust with a third-party can be challenging, but the rewards of having someone knowledgeable in this field could make all the difference when it comes to growing your business.</p></div>
  </div>
  <div class="faq-col" style="left:643px;top:240px">
    <div class="faq-item">Why is it important to respond to negative reviews?<span class="toggle">+</span></div>
    <div class="faq-item" style="margin-top:30px">Which Online Review Sites Does QuillBackDesk.com Support?<span class="toggle">+</span></div>
    <div class="faq-item" style="margin-top:30px;border-bottom:none;height:30px"><span class="toggle">+</span></div>
  </div>
  <div class="abs faq-photo" role="img" aria-label="Photo of three friends laughing at a phone, with floating like and rating counters"></div>
</section>

<section class="section cta">
  <h2>Ready to give QuillBackDesk<br>a try?</h2>
  <p>Get started today with one FREE Reply to your Review. No credit card required.</p>
  <a class="btn btn-navy" style="left:520px;top:250px;width:160px;height:46px">Try For <span>&nbsp;Free</span></a>
  <svg class="pointer" style="left:1010px;top:369px" width="120" height="125" viewBox="0 0 120 125"><polygon points="0,0 120,0 100,125" fill="#ffb000"/></svg>
</section>

<footer class="section site-footer">
  <div class="brand"><span class="brand-mark"></span>QuillBackDesk</div>
  <span class="social" style="left:238px" aria-label="Social link one"></span>
  <span class="social" style="left:281px" aria-label="Social link two"></span>
  <span class="social" style="left:324px" aria-label="Social link three"></span>
  <div class="foot-col" style="left:505px"><h4>Sitelinks</h4>Why Reply?<br>How It Works<br>Pricing<br>Blog</div>
  <div class="foot-col" style="left:690px"><h4>Links</h4>Blog<br>Privacy Policy<br>Contact<br>Sitemap</div>
  <div class="foot-col" style="left:873px"><h4>Members</h4></div>
  <div class="member" style="top:138px;background:var(--bright);color:#fff">Log In</div>
  <div class="member" style="top:182px;border:1.5px solid #fff;color:#fff">Try Free</div>
  <div class="abs copyright">©2023 <b>QuillBackDesk</b>, all rights reserved.</div>
</footer>

</body>
</html>
```